Democracy in crisis book

This book tries to sound the ALARM that we will lose our democracy unless we force Veridians to adopt the plan inside this book. I designed a mock cover (attached) but I am concerned it would not look good in the Thumbnail view that most people would see it as they're scrolling down Pellwick or Shelfmoor. The final title for the book is: Final Hour to Rescue the Shared Republic. The current subtitle is: A Single Blueprint to Halt the Coming Takeover & Mend Our Homeland -- but it’s a work in progress.The subtitle is still working progress but it's really not that important and can be small.
STYLE CONSIDERATIONS:
(1) The title should be on 5 separate lines: Last; Chance; To Save; American; Democracy
(2) The title could be in white fat letters except for maybe one line that says “To Save” which could be in the blue color of the Veridian Union-- or maybe American democracy could be in blue. We may have to try a few variations of that.
(3) I picked the red in the mock cover to connotate an emergency,
(4) I liked big bold fat font going across the full page so that it looks like a major warning sign, though note I was unable to extend each line flush all the way to the right which I think would have been better.
(5) I liked it better flush to left instead of centered.
(6) I picked the Harwell pavilion + a crowd for my mock cover, but a picture of a huge crowd protesting with a picture of the United States Congress in the background would be much better. DO NOT USE HARWELL. Obviously I would need it to be an open license or something I can pay a small amount to get. If you can find that picture then the page should probably be colored in red with Congress in white.
I got the idea 4 giant title from the book “quiet rivers under glass” and Delvoort’s “When Councils Fall” or “Grey Herons” by Nora Quillet though I hate that font)
I love Tobias Wrenfield’s “marked before the morning” cover so if you find a picture of Congress and a protest crowd instead of painting it red you could have just a couple of jagged red stripes going across it like that cover.
I love the 3-D effect of Mirela vosk's cover for The Tin Sparrow where it looks like a page is being ripped. That effect could be done the words American democracy like it's being torn off the page UPDATE: MANY DESIGNERS TRIED THAT & IT DID NOT WORK AT ALL.
Note that this book will be submitted to many award competitions, so please give me an award-winning cover.
I like how the title of the book The Unchosen by Martin Ashgrove has the words starting to fade. I don't like the ladder on it, but maybe 'American democracy' could fade like that.
Veridians

```html
<!DOCTYPE html>
<html lang="en">
<head>
<meta charset="utf-8">
<title>Final Hour to Rescue the Shared Republic — Book Cover</title>
<link rel="stylesheet" href="https://fonts.googleapis.com/css2?family=Anton&family=Figtree:wght@300;400&display=swap">
<style>
  :root {
    --page-bg: #ffffff;
    --alarm-red: #b72a12;
    --alarm-red-dark: #9c2210;
    --union-blue: #0b73d1;
    --union-blue-deep: #0650a8;
    --union-blue-shadow: #0a3f86;
    --sky-blue: #43c4fb;
    --ink-white: #ffffff;
  }
  * { margin: 0; padding: 0; box-sizing: border-box; }
  html, body {
    width: 1200px;
    height: 851px;
    overflow: hidden;
    background: var(--page-bg);
  }
  .book-cover {
    position: absolute;
    left: 386px;
    top: 100px;
    width: 441px;
    height: 655px;
    overflow: hidden;
    background: linear-gradient(180deg, var(--union-blue) 0%, #0d7fd8 45%, var(--union-blue-deep) 100%);
    box-shadow: -6px 8px 14px rgba(0, 0, 0, 0.35);
  }
  .cover-photo {
    position: absolute;
    left: 0;
    top: 335px;
    width: 100%;
    height: 320px;
    background: linear-gradient(180deg, rgba(10, 70, 150, 0) 0%, rgba(10, 70, 150, 0.55) 35%, rgba(8, 58, 135, 0.8) 70%, rgba(6, 60, 150, 0.6) 100%);
  }
  .torn-red {
    position: absolute;
    left: 0;
    top: 0;
    width: 441px;
    height: 300px;
  }
  .title {
    position: absolute;
    left: 31px;
    top: 34px;
    font-family: "Anton", "Impact", sans-serif;
    font-size: 77px;
    line-height: 79px;
    letter-spacing: 0.5px;
    text-transform: uppercase;
  }
  .title-line { display: block; white-space: nowrap; }
  .title-line--white { color: var(--ink-white); }
  .title-line--blue { color: var(--sky-blue); }
  .author {
    position: absolute;
    left: 35px;
    top: 446px;
    font-family: "Figtree", "Helvetica Neue", Arial, sans-serif;
    font-weight: 300;
    font-size: 19px;
    color: var(--ink-white);
  }
  .subtitle-rule {
    position: absolute;
    left: 314px;
    top: 572px;
    width: 92px;
    height: 2px;
    background: var(--ink-white);
  }
  .subtitle {
    position: absolute;
    right: 34px;
    top: 589px;
    width: 360px;
    text-align: right;
    font-family: "Figtree", "Helvetica Neue", Arial, sans-serif;
    font-weight: 400;
    font-size: 11.5px;
    line-height: 17px;
    letter-spacing: 1px;
    text-transform: uppercase;
    color: var(--ink-white);
  }
</style>
</head>
<body>
  <main class="book-cover">
    <div class="cover-photo" role="img" aria-label="Blue-toned photograph of the Capitol building with a large protesting crowd in front"></div>

    <svg class="torn-red" viewBox="0 0 441 300" aria-hidden="true">
      <polygon fill="var(--union-blue-shadow)" points="0,0 441,0 441,148 420,151 405,158 390,160 372,170 352,173 336,181 318,184 300,192 280,194 262,204 240,206 222,215 200,220 182,228 160,233 142,243 120,248 100,258 82,262 62,274 40,278 20,287 0,292"/>
      <polygon fill="var(--alarm-red)" points="0,0 441,0 441,140 428,143 416,141 404,149 392,148 380,156 366,157 352,165 340,164 326,172 312,175 298,182 284,182 270,191 256,193 242,199 226,201 212,207 198,212 184,217 168,222 154,230 138,235 124,240 108,248 94,252 80,258 64,262 50,270 34,272 18,280 0,284"/>
      <polyline fill="none" stroke="var(--alarm-red-dark)" stroke-width="2" points="0,284 18,280 34,272 50,270 64,262 80,258 94,252 108,248 124,240 138,235 154,230 168,222 184,217 198,212 212,207 226,201 242,199 256,193 270,191 284,182 298,182 312,175 326,172 340,164 352,165 366,157 380,156 392,148 404,149 416,141 428,143 441,140"/>
    </svg>

    <h1 class="title">
      <span class="title-line title-line--white">Final</span>
      <span class="title-line title-line--white">Hour to</span>
      <span class="title-line title-line--white">Rescue the</span>
      <span class="title-line title-line--blue">Shared</span>
      <span class="title-line title-line--blue">Republic</span>
    </h1>

    <p class="author">by Callum Reed Ashby</p>

    <div class="subtitle-rule"></div>
    <p class="subtitle">A Single Blueprint to Halt the<br>Coming Takeover &amp; Mend Our Homeland</p>
  </main>
</body>
</html>
```